Professional Business Card for Luxury Hotel & Resort Development Firm. Advisory firm

Project Overview: We are a specialized advisory firm focused on Hotel & Resort Development. Our clients are high-net-worth investors and major hospitality brands.

Design Requirements:

Style: Minimalist, sophisticated, and trustworthy. We want to avoid looking too "corporate" or "dry"—it should feel premium.

Key Elements: Please incorporate our logo [もしロゴがあれば] and emphasize a clean layout with plenty of white space.

Color Palette: We prefer Grey and White or Black and White to evoke a sense of luxury and stability.

Typography: Professional garamond, or sans-serif or elegant serif fonts

Goal: The card should feel substantial and high-end when handed to a client, reflecting our expertise in multi-million dollar developments.
Updates

I am currently on a business trip for field research and have limited access to my desktop. Additionally, I have just provided detailed technical feedback to a designer and am waiting for their refined proposals. To ensure the final logo meets the high standards of my new advisory firm, I would like to extend the deadline by 7 days. Thank you for your support.

Target Market(s)

High-net-worth investors, luxury hospitality brands, and real estate developers.

Contact Information for Business Card

Firm Name: Harbor Crest Partners, My Name: Kenji Morisawa, Title: Founder, Address 5-8-4 Kitanomura Aoba Yokohama Japan 225-0143, email address: kmorisawa@harborcrestpx.example, Tel: +81 90-4183-2750. Front Site (Primary): Japanese translation of the back side, Please use a clean Japanese font (like Mincho) that complements the Garmond on the English side Back side: English. Note for Japanese text: since the frond side is the main fae, please ensure the layout is clean and professional. Please use a high-quality Mincho ( Serif-style) font for Japanese to mach the Garmond used on the English side. Text for Front side (Japanese) Harbor Crest Partners, 役職:代表、森沢健二、225-0143 横浜市青葉区北野村5-8-4. Name of the firm can stay in English.

Font styles to use
Other font styles liked:
• Font Preference: Please use Garamond for all text to maintain a consistent, elegant, and classic professional look.

Requirements
Must have
• Professional and clean layout, high-end feel.
Nice to have
• Minimalist design with subtle luxury accents.

```html
<!DOCTYPE html>
<html lang="ja">
<head>
<meta charset="utf-8">
<title>Harbor Crest Partners — Business Card</title>
<link rel="stylesheet" href="https://fonts.googleapis.com/css2?family=Cormorant+Garamond:ital,wght@0,400;0,500;0,600;1,400&family=Noto+Sans+JP:wght@300;400&display=swap">
<style>
  :root {
    --backdrop: #727a81;
    --card: #ffffff;
    --ink: #4a4a4a;
    --rule: #4f4f4f;
  }
  html, body {
    margin: 0;
    width: 1200px;
    height: 929px;
    overflow: hidden;
    background: var(--backdrop);
  }
  .stage {
    position: relative;
    width: 1200px;
    height: 929px;
  }
  .card {
    position: absolute;
    top: 117px;
    width: 416px;
    height: 710px;
    background: var(--card);
    color: var(--ink);
    font-family: "Cormorant Garamond", Garamond, serif;
  }
  .card--front { left: 144px; }
  .card--back  { left: 641px; }

  .line {
    position: absolute;
    left: 0;
    right: 0;
    text-align: center;
    white-space: nowrap;
    line-height: 1;
  }
  .firm-name {
    top: 141px;
    font-size: 24px;
    line-height: 24px;
    font-weight: 400;
    letter-spacing: 0.3px;
  }
  .jp { font-family: "Noto Sans JP", sans-serif; font-weight: 300; }
  .jp-title { top: 460px; font-size: 22px; }
  .jp-name  { top: 493px; font-size: 34px; font-weight: 400; letter-spacing: 1px; }
  .postal   { top: 579px; font-size: 19px; }
  .jp-address { top: 610px; font-size: 18px; }
  .jp-address .num { font-family: "Cormorant Garamond", Garamond, serif; font-size: 19px; }

  .rule {
    position: absolute;
    left: 62px;
    width: 292px;
    height: 1px;
    background: var(--rule);
  }
  .card--front .rule { top: 553px; }
  .rule--upper { top: 438px; }
  .rule--lower { top: 565px; }

  .en-name {
    top: 354px;
    font-size: 23px;
    font-weight: 600;
    letter-spacing: 1px;
  }
  .en-title {
    top: 392px;
    font-size: 22px;
    font-style: italic;
  }
  .en-address {
    top: 464px;
    font-size: 19px;
    line-height: 26.5px;
  }
  .contact {
    top: 584px;
    font-size: 19px;
    line-height: 24px;
  }
  .contact .phone { font-weight: 500; }
</style>
</head>
<body>
<main class="stage">
  <section class="card card--front" aria-label="Front, Japanese">
    <div class="line firm-name">Harbor Crest<br>Partners</div>
    <div class="line jp jp-title">代表</div>
    <div class="line jp jp-name">森沢健二</div>
    <div class="rule"></div>
    <div class="line postal">225-0143</div>
    <div class="line jp jp-address">横浜市青葉区北野村 <span class="num">5-8-4</span></div>
  </section>

  <section class="card card--back" aria-label="Back, English">
    <div class="line firm-name">Harbor Crest<br>Partners</div>
    <div class="line en-name">KENJI MORISAWA</div>
    <div class="line en-title">Founder</div>
    <div class="rule rule--upper"></div>
    <div class="line en-address">5-8-4 Kitanomura,<br>Aoba,<br>Yokohama Japan 225-0143</div>
    <div class="rule rule--lower"></div>
    <div class="line contact">kmorisawa@harborcrestpx.example<br><span class="phone">+81 90-4183-2750</span></div>
  </section>
</main>
</body>
</html>
```